Newspaper ad advertising bathroom adaptations for the less-abled and disabled.

This ad is to really promote bathroom adaptations that are suited to the clients needs, so more care led rather than design led. Important for the ad to be easy to read and easy to understand. Clearly states bathroom conversions from £4,999 to help qualify leads generated from the ad. We are looking to reach out to anyone whose bathroom is becoming more challenging because of mobility issues so we can use our excellent industry knowledge and personal family experience to come up with solutions that really work for the client

Target Market(s)

predominately older people

Industry/Entity Type

Health And Wellness

Font styles to use
Serif

Colors

Designer to choose colors to be used in the design.

Requirements
Must have
• It must have the content that is included in advert i have attached. Use where possible the photos of the actual jobs we've done to make it relatable for the client to see real jobs.
Nice to have
• some added pictures of mobility bathroom equipment including walk-in baths, walk-in showers and wetroom flooring.
Should not have
• anything too heavy on the eye.

```html
<!DOCTYPE html>
<html lang="en">
<head>
<meta charset="utf-8">
<title>Harbourside Adaptations – Bathroom Adaptations</title>
<link href="https://fonts.googleapis.com/css2?family=Lato:ital,wght@0,400;0,700;0,900;1,400;1,700;1,900&display=swap" rel="stylesheet">
<style>
  :root{
    --navy:#1b2f6e;
    --navy-deep:#0e2160;
    --blue:#1f4aa3;
    --orange:#f26a21;
    --teal:#1fb3a6;
    --white:#ffffff;
    --text-navy:#1d3170;
    --photo-green:#3f6b58;
    --photo-dark:#1e2b34;
  }
  *{box-sizing:border-box;margin:0;padding:0}
  html,body{width:904px;height:1200px;overflow:hidden;background:#e9e9e9}
  body{font-family:"Lato",Arial,sans-serif}
  .ad{position:relative;width:904px;height:1200px;overflow:hidden;background:var(--white)}
  .hero-photo{position:absolute;left:0;top:0;width:904px;height:560px;
    background:linear-gradient(120deg,var(--photo-dark) 0%,#2f4a46 35%,var(--photo-green) 60%,#5b7f6d 80%,#8aa49a 100%)}
  .hero-shade{position:absolute;left:0;top:0;width:904px;height:560px;
    background:linear-gradient(90deg,rgba(14,33,96,.85) 0%,rgba(14,33,96,.55) 40%,rgba(14,33,96,0) 65%),
               linear-gradient(180deg,rgba(14,33,96,.7) 0%,rgba(14,33,96,0) 30%)}
  .shapes{position:absolute;left:0;top:0}
  .headline{position:absolute;left:18px;top:88px;width:360px;text-align:center;color:var(--white)}
  .headline h1{font-weight:900;font-size:29px;line-height:1.2;text-transform:uppercase}
  .headline .solution{font-weight:900;font-size:25px;margin-top:16px}
  .headline .for-whom{font-style:italic;font-weight:700;color:var(--orange);font-size:17px;line-height:1.25;margin-top:12px}
  .quote{position:absolute;left:400px;top:84px;width:490px;text-align:center;color:var(--white);
    font-style:italic;font-weight:700;font-size:30px;line-height:1.3}
  .price-burst{position:absolute;left:132px;top:318px;width:210px;height:210px;background:var(--orange);
    clip-path:polygon(100% 50%,93.2% 58.6%,96.2% 69.2%,86.6% 74.5%,85.4% 85.4%,74.5% 86.6%,69.2% 96.2%,58.6% 93.2%,50% 100%,41.4% 93.2%,30.8% 96.2%,25.5% 86.6%,14.6% 85.4%,13.4% 74.5%,3.8% 69.2%,6.8% 58.6%,0% 50%,6.8% 41.4%,3.8% 30.8%,13.4% 25.5%,14.6% 14.6%,25.5% 13.4%,30.8% 3.8%,41.4% 6.8%,50% 0%,58.6% 6.8%,69.2% 3.8%,74.5% 13.4%,85.4% 14.6%,86.6% 25.5%,96.2% 30.8%,93.2% 41.4%);
    display:flex;flex-direction:column;align-items:center;justify-content:center;color:var(--white);text-align:center;font-weight:900}
  .price-burst .label{font-size:23px;line-height:1.15}
  .price-burst .amount{font-size:32px;margin-top:4px}
  .price-burst sup{font-size:17px}
  .brand{position:absolute;left:30px;top:560px;display:flex;align-items:center;gap:12px}
  .brand-mark{width:40px;height:40px;background:var(--teal)}
  .brand-name{font-weight:900;font-size:31px;color:var(--text-navy)}
  .services{position:absolute;left:30px;top:642px;width:430px;list-style:none}
  .services li{position:relative;padding-left:22px;font-size:13.6px;font-weight:700;color:var(--text-navy);line-height:22.6px}
  .services li::before{content:"";position:absolute;left:0;top:5px;width:12px;height:12px;border:1.6px solid var(--teal);border-radius:50%}
  .services li::after{content:"";position:absolute;left:4px;top:7.5px;width:3px;height:6px;border:solid var(--orange);border-width:0 2px 2px 0;transform:rotate(45deg)}
  .badges{position:absolute;left:30px;top:1038px;display:flex;gap:14px;align-items:center}
  .badge{background:#d9dde6}
  .badge.rect{width:62px;height:44px;border-radius:4px;background:#c9cfdc}
  .badge.round{width:46px;height:46px;border-radius:50%;background:#9fc3e6}
  .badge.wide{width:96px;height:44px;background:#b5a0cf;border-radius:4px}
  .badge.long{width:150px;height:46px;background:#e1c05a;border-radius:4px}
  .offer{position:absolute;left:486px;top:560px;width:400px;color:var(--white)}
  .offer h2{font-weight:900;font-size:26.5px;line-height:1.17;color:var(--orange);text-transform:uppercase}
  .offer h2 .price{color:var(--teal)}
  .offer h2 sup{font-size:15px}
  .offer .care{font-style:italic;font-weight:700;font-size:16px;line-height:1.3;margin-top:18px;width:340px}
  .offer .cta{font-style:italic;font-weight:900;font-size:16px;line-height:1.35;color:var(--teal);margin-top:34px;text-transform:uppercase}
  .job-photo{position:absolute;border-radius:50%;border:5px solid var(--white);box-shadow:0 2px 6px rgba(0,0,0,.3)}
  .job-photo.basin{left:438px;top:930px;width:178px;height:178px;background:radial-gradient(circle at 50% 45%,#f2f2f2 0%,#c9cfc9 35%,#4f7563 70%,#34524a 100%)}
  .job-photo.seat{left:640px;top:920px;width:192px;height:192px;background:radial-gradient(circle at 50% 50%,#f7f7f7 0%,#dfe3e6 55%,#b5bec4 100%)}
  .phone{position:absolute;left:530px;top:1124px;display:flex;align-items:center;gap:10px;color:var(--teal);font-weight:900;font-size:44px}
</style>
</head>
<body>
<div class="ad">
  <div class="hero-photo" role="img" aria-label="Photograph of a completed walk-in shower room with green tiles, glass screen and wall-hung basin"></div>
  <div class="hero-shade"></div>

  <svg class="shapes" width="904" height="1200" viewBox="0 0 904 1200" aria-hidden="true">
    <defs>
      <linearGradient id="panelBlue" x1="0" y1="0" x2="0" y2="1">
        <stop offset="0" stop-color="#1f4aa3"/>
        <stop offset="1" stop-color="#0e2160"/>
      </linearGradient>
    </defs>
    <path d="M0,405 C160,475 330,505 520,470 C680,440 800,380 904,340 L904,1200 L0,1200 Z" fill="var(--navy)"/>
    <path d="M0,425 C160,495 330,525 520,490 C680,460 800,400 904,360 L904,1200 L0,1200 Z" fill="var(--teal)"/>
    <path d="M0,445 C160,515 330,545 520,510 C680,480 800,420 904,380 L904,1200 L0,1200 Z" fill="var(--white)"/>
    <path d="M467,516 C620,495 780,435 904,385 L904,1200 L467,1200 Z" fill="url(#panelBlue)"/>
    <path d="M0,1090 C160,1050 330,1065 467,1130 L467,1200 L0,1200 Z" fill="var(--teal)"/>
    <path d="M0,1112 C160,1078 330,1092 467,1150 L467,1200 L0,1200 Z" fill="var(--navy-deep)"/>
  </svg>

  <div class="headline">
    <h1>Is your bathroom becoming more challenging?</h1>
    <p class="solution">We Have The Solution...</p>
    <p class="for-whom">Bathroom adaptations for the<br>elderly, disabled and less abled</p>
  </div>

  <p class="quote">” from concept to creation to completion... we do it all”</p>

  <div class="price-burst">
    <span class="label">MOBILITY<br>NEEDS FROM</span>
    <span class="amount">£4,999<sup>*</sup></span>
  </div>

  <div class="brand">
    <span class="brand-mark"></span>
    <span class="brand-name">Harbourside Adaptations</span>
  </div>

  <ul class="services">
    <li>Existing bathroom to wetroom conversions</li>
    <li>Walk-in showers &amp; wetrooms tailored to meet your needs</li>
    <li>Full bathroom mobility enablement</li>
    <li>Free no obligation home assessment</li>
    <li>Full detailed pre-install survey</li>
    <li>Fully project managed dedicated installation team</li>
    <li>Full insurance backed guarantee on all adaptations</li>
    <li>All tiling, electrics, plumbing etc carried out</li>
    <li>Bathing enabling equipment</li>
    <li>Work closely with occupational therapists</li>
    <li>Anti-slip safety flooring</li>
    <li>Maintenance free shower panelling</li>
    <li>Walk-in easy access baths</li>
    <li>Specialist wash &amp; dry toilets</li>
    <li>Fully accredited to HomeCheck, NMTA<br>and the Fair Trade Guild</li>
  </ul>

  <div class="badges" aria-hidden="true">
    <span class="badge rect"></span>
    <span class="badge round"></span>
    <span class="badge wide"></span>
    <span class="badge long"></span>
  </div>

  <div class="offer">
    <h2>Adapted bathroom conversions to help with your mobility needs from <span class="price">£4,999<sup>*</sup></span></h2>
    <p class="care">we care passionately about installing a quality bathroom that really works for your needs</p>
    <p class="cta">Call us today for a free no obligation home assessment</p>
  </div>

  <div class="job-photo basin" role="img" aria-label="Photograph of a wall-mounted vessel basin in a tiled wetroom"></div>
  <div class="job-photo seat" role="img" aria-label="Photograph of a white shower seat with grab rails"></div>

  <div class="phone">
    <svg width="40" height="40" viewBox="0 0 24 24" aria-hidden="true">
      <path fill="currentColor" d="M6.6 10.8c1.4 2.8 3.8 5.1 6.6 6.6l2.2-2.2c.3-.3.7-.4 1-.2 1.1.4 2.3.6 3.6.6.6 0 1 .4 1 1V20c0 .6-.4 1-1 1C10.6 21 3 13.4 3 4c0-.6.4-1 1-1h3.5c.6 0 1 .4 1 1 0 1.3.2 2.5.6 3.6.1.3 0 .7-.2 1z"/>
    </svg>
    <span>0800 000 4321</span>
  </div>
</div>
</body>
</html>
```